THE WELLNESS BARN WEBSITE for Physio, Fitness, health

An attractive website advertising a physiotherapyand fitness / gym business, not generic, colours are natural, greens, browns, beiges. No cheesy pictures. With the ability to sell a small,amount of goods online if i decide to. Simple to navigate. Text boxes that i can input the main information and change easily. Somewhere to put my timetable. Easy to find contact details. However many pages it needs, im not fussed.
Target Market(s)
People looking for rehabilitation or fitness classes
Industry/Entity Type
Physiotherapy, Fitness, Gym, Health
Coding
Coded - Design and coding required
Number of Pages Required
1 page
Font styles to use
Other font styles liked:
- Im not fusse,ld, not script
Requirements
Must have
- Will upload posts from my business insta page for reference about the feel. Earthy natural tones, I have a lot of timber, and rustic looking piece's, plants etc in my clinic
Nice to have
- Simple to navigate
Should not have
- Cheesy "yoga" or generic "people doing physio" pics

```html
<!DOCTYPE html>
<html lang="en">
<head>
<meta charset="utf-8">
<title>The Wellness Barn — Physiotherapy, Rehabilitation &amp; Fitness</title>
<link href="https://fonts.googleapis.com/css2?family=Oswald:wght@500;600&family=Cinzel:wght@400&family=Great+Vibes&family=Roboto:wght@400;500&display=swap" rel="stylesheet">
<style>
:root{
  --cream:#f8f5ec;
  --beige:#eee7d3;
  --beige-line:#ffffff;
  --green:#2e4a1f;
  --green-soft:#8b9a6b;
  --brown:#5b2d0f;
  --bark:#5a4a3c;
  --ink:#3b3a30;
  --muted:#6a665a;
  --night:#0e120c;
  --star:#e59a1c;
  --white:#ffffff;
}
*{box-sizing:border-box;margin:0;padding:0}
html,body{width:1200px;height:4351px;overflow:hidden}
body{position:relative;background:var(--cream);font-family:"Roboto",Arial,sans-serif;color:var(--ink)}
.abs{position:absolute}
.script{font-family:"Great Vibes",cursive;color:var(--bark);opacity:.28;font-size:44px;line-height:1}
.heading{font-family:"Oswald",Arial,sans-serif;font-weight:600;color:var(--green);font-size:33px;line-height:1;letter-spacing:.3px;text-transform:uppercase}
.center{left:0;width:1200px;text-align:center}
.btn{position:absolute;display:flex;align-items:center;justify-content:center;background:var(--green);color:var(--white);font-size:13px;border-radius:3px}
.body-text{font-size:13.5px;line-height:23px;color:var(--ink)}

/* hero */
.hero-photo{left:0;top:0;width:1200px;height:642px;background:linear-gradient(180deg,#7ea6c9 0%,#a9c2c8 22%,#55703e 45%,#3f5a2c 62%,#6f8c72 78%,#a3b8a6 100%)}
.hero-wave{left:0;top:520px;width:1200px;height:140px}
.nav{left:144px;top:59px;width:912px;height:47px;background:var(--white);border-radius:24px}
.nav a{position:absolute;top:17px;font-size:12px;color:#222;text-decoration:none;text-transform:uppercase}
.nav .nav-cta{top:5px;height:37px;width:124px;background:var(--brown);color:var(--white);border-radius:19px;display:flex;align-items:center;justify-content:center;font-size:12px}
.brand-badge{left:532px;top:13px;width:136px;height:136px;border-radius:50%;background:var(--white);border:4px solid var(--green);display:flex;align-items:center;justify-content:center;text-align:center}
.brand-badge span{font-family:"Oswald",Arial,sans-serif;font-weight:600;font-size:19px;line-height:22px;color:var(--green)}
.hero-script{top:185px;font-family:"Great Vibes",cursive;font-size:60px;color:rgba(255,255,255,.75)}
.hero-title{top:278px;font-family:"Cinzel",Georgia,serif;font-size:42px;line-height:46px;color:var(--white);letter-spacing:1px}
.hero-btn{top:400px;height:48px;font-size:13px;text-transform:uppercase;letter-spacing:.5px}
.hero-btn.book{left:404px;width:196px;background:var(--green);color:var(--white)}
.hero-btn.contact{left:620px;width:196px;background:var(--white);color:var(--green)}

/* about */
.about-photo{left:160px;top:705px;width:390px;height:395px;background:radial-gradient(circle at 45% 50%,#8a8a82 0%,#6c6b63 45%,#c9c4b6 75%,rgba(248,245,236,0) 76%)}
.about-wood{left:400px;top:990px;width:85px;height:85px;border-radius:50%;background:radial-gradient(circle,#d8a86a 0%,#b07a42 70%,#7a4b24 100%)}
.about-plant{left:452px;top:980px;width:100px;height:100px;border-radius:50%;background:radial-gradient(circle,#5c8a3a,#2e5520)}

/* services */
.card{top:1300px;width:212px;height:282px;border:1px solid #ddd6c4;border-radius:6px;background:var(--cream)}
.card.active{background:var(--green);border-color:var(--green)}
.card .icon{position:absolute;left:16px;top:30px;width:84px;height:84px;border-radius:50%;display:flex;align-items:center;justify-content:center}
.card h3{position:absolute;left:16px;top:138px;font-size:14.5px;font-weight:500;text-transform:uppercase}
.card p{position:absolute;left:16px;top:165px;width:185px;font-size:12.5px;line-height:23px;color:var(--ink)}
.card .more{position:absolute;left:16px;top:227px;font-size:12.5px}
.card.active h3,.card.active p,.card.active .more{color:var(--white)}

/* timetable */
.log{border-radius:50%;background:radial-gradient(circle,#e2b47a 0%,#c48b4c 55%,#8a5527 90%,#6d401c 100%)}
.log-plant{border-radius:50%;background:radial-gradient(circle,#6a9a45 0%,#3c6a28 60%,#b07a42 75%,#7a4b24 100%)}
.timetable{left:142px;top:1911px;width:916px;border-collapse:collapse;table-layout:fixed;background:var(--beige);box-shadow:0 4px 12px rgba(0,0,0,.12)}
.timetable th,.timetable td{height:34.7px;border:1px solid var(--beige-line);font-size:12.5px;font-weight:400;text-align:center;color:var(--ink)}
.timetable th{height:38px;background:#e6dcc0}
.timetable .hl{background:var(--green);color:var(--white)}

/* why */
.feature-icon{left:140px;width:58px;height:58px}
.feature-title{left:213px;font-size:15px;font-weight:500;color:var(--green);text-transform:uppercase}
.feature-text{left:213px;width:340px;font-size:12.5px;line-height:24px;color:var(--ink)}
.why-photo{left:620px;top:2370px;width:436px;height:400px;background:radial-gradient(ellipse at 50% 50%,#a8885a 0%,#8b6a3e 45%,#c9ad7f 70%,rgba(248,245,236,0) 72%)}

/* testimonials */
.quote{width:281px;text-align:center;font-size:12.5px;line-height:23px;color:var(--ink)}
.profile{height:59px;width:281px;background:var(--white);box-shadow:0 2px 8px rgba(0,0,0,.06)}
.avatar{position:absolute;left:12px;top:-6px;width:66px;height:66px;border-radius:50%;border:4px solid var(--white);background:linear-gradient(160deg,#c9a98a,#7a5a42);box-shadow:0 2px 6px rgba(0,0,0,.15)}
.profile .name{position:absolute;left:92px;top:14px;font-size:14px;font-weight:500;color:var(--ink)}
.profile .role{position:absolute;left:92px;top:33px;font-size:11px;color:var(--muted)}
.profile .stars{position:absolute;right:14px;top:19px;font-size:13px;letter-spacing:2px;color:var(--star)}
.feature-card{left:460px;top:2961px;width:281px;height:230px;background:var(--green);border-radius:4px;box-shadow:0 8px 20px rgba(0,0,0,.2)}
.feature-card .quote{position:absolute;left:0;top:22px;padding:0 18px;color:var(--white)}
.feature-card .profile{position:absolute;left:0;top:169px;background:var(--green-soft);box-shadow:none}
.feature-card .name,.feature-card .role{color:var(--white)}
.arrow{width:36px;height:36px;border-radius:50%;background:var(--white);box-shadow:0 2px 8px rgba(0,0,0,.12);display:flex;align-items:center;justify-content:center}

/* gallery */
.tile{border-radius:6px}

/* footer */
.footer{left:0;top:3912px;width:1200px;height:381px;background:var(--night)}
.footer-edge{left:0;top:3880px;width:1200px;height:60px}
.footer-brand{left:144px;top:4120px;width:220px;font-family:"Oswald",Arial,sans-serif;font-weight:600;font-size:34px;line-height:40px;color:#2f4a22}
.footer h4{position:absolute;top:4067px;font-size:14.5px;font-weight:500;color:var(--white);text-transform:uppercase}
.footer-link{position:absolute;left:406px;font-size:12.5px;color:var(--white)}
.contact-row{position:absolute;left:597px;font-size:12.5px;line-height:18px;color:var(--white)}
.contact-row svg{position:absolute;left:0;top:2px}
.contact-row div{margin-left:24px}
.map{left:858px;top:4107px;width:200px;height:131px;border-radius:6px;background:linear-gradient(135deg,#eef0ea,#d9e2d8)}
.bottom-bar{left:0;top:4293px;width:1200px;height:58px;background:var(--green-soft)}
.bottom-bar p{position:absolute;left:122px;top:21px;font-size:12px;color:#1c1c16}
.social{top:4307px;width:30px;height:30px;border-radius:50%;background:#11140e}
</style>
</head>
<body>

<!-- HERO -->
<section>
  <div class="abs hero-photo" role="img" aria-label="Photograph of a forest river valley with pine trees, granite cliffs and a waterfall"></div>
  <svg class="abs hero-wave" viewBox="0 0 1200 140" preserveAspectRatio="none" aria-hidden="true">
    <path d="M0 80 C120 70 200 40 300 45 C360 48 420 30 480 38 C600 55 700 95 840 92 C960 90 1060 60 1200 70 L1200 140 L0 140 Z" fill="var(--cream)"/>
    <path d="M0 100 C200 95 360 70 520 80 C700 92 900 110 1200 95 L1200 140 L0 140 Z" fill="#efeadb"/>
  </svg>

  <nav class="abs nav">
    <a style="left:50px">Home</a>
    <a style="left:152px">About Us</a>
    <a style="left:277px">Services</a>
    <a style="left:575px">Timetable</a>
    <a style="left:688px">Gallery</a>
    <a class="nav-cta" style="left:789px">Contact Us</a>
  </nav>
  <div class="abs brand-badge"><span>THE<br>WELLNESS<br>BARN</span></div>

  <div class="abs center hero-script">Physiotherapy</div>
  <h1 class="abs center hero-title" style="font-weight:400">REHABILITATION<br>&amp; FITNESS – NATURALLY</h1>
  <div class="btn hero-btn book">Book Your Session</div>
  <div class="btn hero-btn contact">Contact Us</div>
</section>

<!-- ABOUT -->
<section>
  <div class="abs about-photo" role="img" aria-label="Photograph of a trainer from behind in a branded t-shirt working at gym equipment"></div>
  <div class="abs about-wood" role="img" aria-label="Timber log slice decoration"></div>
  <div class="abs about-plant" role="img" aria-label="Potted fern decoration"></div>

  <div class="abs script" style="left:650px;top:736px">Who We Are</div>
  <h2 class="abs heading" style="left:645px;top:765px">About The Wellness Barn</h2>
  <p class="abs body-text" style="left:645px;top:812px;width:410px">Lorem ipsum dolor sit amet, consectetuer adipiscing elit, sed diam nonummy nibh euismod tincidunt ut laoreet dolore magna aliquam erat volutpat. Ut wisi enim ad minim veniam, quis nostrud exerci tation ullamcorper suscipit lobortis nisl ut aliquip ex ea commodo consequat. Duis autem vel eum iriure dolor in hendrerit in vulputate velit esse molestie consequat, vel illum dolore eu feugiat nulla facilisis at vero eros et accumsan et iusto odio dignissim qui blandit praesent luptatum zzril delenit augue duis dolore te feugait nulla facilisi.</p>
  <div class="btn" style="left:645px;top:1016px;width:107px;height:35px">Read More</div>
</section>

<!-- SERVICES -->
<section>
  <div class="abs script center" style="top:1200px">What We Do</div>
  <h2 class="abs heading center" style="top:1230px">Our Services</h2>

  <article class="abs card" style="left:142px">
    <div class="icon" style="background:var(--brown)">
      <svg width="40" height="40" viewBox="0 0 40 40" fill="none" stroke="#fff" stroke-width="2"><rect x="6" y="24" width="28" height="6" rx="2"/><path d="M10 30v5M30 30v5M14 20l8-8M18 12h8v8"/></svg>
    </div>
    <h3 style="color:var(--brown)">Physiotherapy</h3>
    <p>Expert care for injury recovery and pain management.</p>
    <span class="more" style="color:var(--brown)">Read More »</span>
  </article>

  <article class="abs card active" style="left:375px">
    <div class="icon" style="background:var(--white)">
      <svg width="40" height="40" viewBox="0 0 40 40" fill="none" stroke="var(--green)" stroke-width="2"><path d="M20 6v10M15 11h10"/><rect x="8" y="22" width="24" height="5" rx="2"/><path d="M12 27l-3 9M28 27l3 9"/></svg>
    </div>
    <h3>Rehabilitation</h3>
    <p>Expert care for injury recovery and pain management.</p>
    <span class="more">Read More »</span>
  </article>

  <article class="abs card" style="left:610px">
    <div class="icon" style="background:var(--green-soft)">
      <svg width="40" height="40" viewBox="0 0 40 40" fill="none" stroke="#fff" stroke-width="2"><path d="M6 20h28"/><rect x="8" y="13" width="5" height="14" rx="1"/><rect x="27" y="13" width="5" height="14" rx="1"/></svg>
    </div>
    <h3 style="color:var(--green-soft)">Fitness Classes</h3>
    <p style="color:var(--muted)">Expert care for injury recovery and pain management.</p>
    <span class="more" style="color:var(--green-soft)">Read More »</span>
  </article>

  <article class="abs card" style="left:845px">
    <div class="icon" style="background:var(--bark)">
      <svg width="40" height="40" viewBox="0 0 40 40" fill="none" stroke="#fff" stroke-width="2"><rect x="8" y="20" width="24" height="12" rx="2"/><path d="M14 20v-6h12v6M20 24v4"/></svg>
    </div>
    <h3 style="color:var(--bark)">Personal Training</h3>
    <p>Expert care for injury recovery and pain management.</p>
    <span class="more" style="color:var(--bark)">Read More »</span>
  </article>

  <div class="btn" style="left:546px;top:1619px;width:106px;height:34px">View All</div>
</section>

<!-- TIMETABLE -->
<section>
  <div class="abs script center" style="top:1762px">Schedule</div>
  <h2 class="abs heading center" style="top:1790px">My Timetable</h2>
  <p class="abs body-text center" style="top:1834px;font-size:13px">Lorem ipsum dolor sit amet, consectetuer adipiscing elit, sed diam nonummy nibh<br>euismod tincidunt ut laoreet dolore magna aliquam erat volutpat.</p>

  <div class="abs log" style="left:1000px;top:1858px;width:102px;height:102px" role="img" aria-label="Timber log slice decoration"></div>
  <div class="abs log-plant" style="left:60px;top:2095px;width:170px;height:170px" role="img" aria-label="Timber log slice with fern leaves decoration"></div>

  <table class="abs timetable">
    <thead>
      <tr><th>Time</th><th>Monday</th><th class="hl">Tuesday</th><th>Wednesday</th><th>Thursday</th><th>Friday</th><th>Saturday</th><th>Sunday</th></tr>
    </thead>
    <tbody>
      <tr><td>07:00-08:30</td><td>Yoga Class</td><td></td><td>Fitness Class</td><td></td><td></td><td>Yoga Class</td><td></td></tr>
      <tr><td>08:30-09:45</td><td>Physiotherapy</td><td></td><td></td><td></td><td></td><td></td><td>Physiotherapy</td></tr>
      <tr><td>09:45-10:30</td><td></td><td></td><td>Yoga Class</td><td></td><td>Strength Training</td><td></td><td></td></tr>
      <tr><td class="hl">10:30-11:30</td><td></td><td class="hl">Strength Training</td><td></td><td>Physiotherapy</td><td></td><td></td><td></td></tr>
      <tr><td>11:30-13:00</td><td></td><td></td><td>Fitness</td><td></td><td></td><td></td><td></td></tr>
      <tr><td>14:00-14:30</td><td></td><td>Yoga Class</td><td></td><td></td><td></td><td></td><td>Strength Training</td></tr>
      <tr><td>16:00-17:00</td><td>Yoga Class</td><td></td><td></td><td>Fitness Class</td><td></td><td>Physiotherapy</td><td></td></tr>
    </tbody>
  </table>

  <div class="btn" style="left:537px;top:2229px;width:107px;height:34px">Book Now</div>
</section>

<!-- WHY CHOOSE US -->
<section>
  <div class="abs script" style="left:148px;top:2378px">Difference</div>
  <h2 class="abs heading" style="left:144px;top:2404px">Why Choose Us?</h2>
  <p class="abs body-text" style="left:144px;top:2451px;width:440px;font-size:13px">Lorem ipsum dolor sit amet, consectetuer adipiscing elit, sed diam nonummy nibh euismod tincidunt ut laoreet dolore magna aliquam erat.</p>

  <svg class="abs feature-icon" style="top:2508px" viewBox="0 0 58 58" fill="none" stroke="var(--brown)" stroke-width="2"><circle cx="20" cy="18" r="7"/><circle cx="38" cy="18" r="7"/><path d="M6 50v-12c0-6 5-10 14-10s14 4 14 10v12M30 28c2-1 5-1 8-1 9 0 14 4 14 10v13"/></svg>
  <div class="abs feature-title" style="top:2512px">Experienced Staff</div>
  <p class="abs feature-text" style="top:2538px">Loreet dolore magna aliquam erat volutpat. Ut wisi enim ad minim veniam, quis nostrud exerci tation.</p>

  <svg class="abs feature-icon" style="top:2602px" viewBox="0 0 58 58" fill="none" stroke="var(--brown)" stroke-width="2"><circle cx="29" cy="29" r="26" fill="#eee7d7" stroke="none"/><path d="M29 46V22M29 40c-8 0-14-6-14-14 8 0 14 6 14 14zM29 36c7 0 12-5 12-12-7 0-12 5-12 12z"/></svg>
  <div class="abs feature-title" style="top:2604px">Natural Environment</div>
  <p class="abs feature-text" style="top:2630px">Loreet dolore magna aliquam erat volutpat. Ut wisi enim ad minim veniam, quis nostrud exerci tation.</p>

  <svg class="abs feature-icon" style="top:2694px" viewBox="0 0 58 58" fill="none" stroke="var(--brown)" stroke-width="2"><circle cx="22" cy="24" r="18" fill="#eee7d7" stroke="none"/><circle cx="22" cy="26" r="11"/><rect x="20" y="28" width="28" height="20" rx="2"/><path d="M25 35h18M25 41h18"/></svg>
  <div class="abs feature-title" style="top:2697px">Personalized Plans</div>
  <p class="abs feature-text" style="top:2723px">Loreet dolore magna aliquam erat volutpat. Ut wisi enim ad minim veniam, quis nostrud exerci tation.</p>

  <div class="abs why-photo" role="img" aria-label="Photograph of branded drink coolers on dried eucalyptus leaves with a timber slice"></div>
</section>

<!-- TESTIMONIALS -->
<section>
  <div class="abs script center" style="top:2876px">Testimonials</div>
  <h2 class="abs heading center" style="top:2902px">Happy Client Sayings</h2>

  <div class="abs arrow" style="left:92px;top:3056px"><svg width="18" height="10" viewBox="0 0 18 10" fill="none" stroke="#444" stroke-width="1.4"><path d="M17 5H1M5 1L1 5l4 4"/></svg></div>
  <div class="abs arrow" style="left:1072px;top:3056px"><svg width="18" height="10" viewBox="0 0 18 10" fill="none" stroke="#444" stroke-width="1.4"><path d="M1 5h16M13 1l4 4-4 4"/></svg></div>

  <p class="abs quote" style="left:142px;top:3016px">Lorem ipsum dolor sit amet, consectetuer adipiscing elit, sed diam nonu mmy nibh euismod tincidunt ut laoreet dolore magna aliquam erat volut pat. Ut wisi enim ad minim veniam, quis nostrud exerci.</p>
  <div class="abs profile" style="left:142px;top:3165px">
    <div class="avatar" role="img" aria-label="Client portrait photo"></div>
    <span class="name">Harper L.</span><span class="role">Lorem ipsum</span><span class="stars">★★★★★</span>
  </div>

  <div class="abs feature-card">
    <p class="quote">Lorem ipsum dolor sit amet, consectetuer adipiscing elit, sed diam nonu mmy nibh euismod tincidunt ut laoreet dolore magna aliquam erat volut pat. Ut wisi enim ad minim veniam, quis nostrud exerci.</p>
    <div class="profile">
      <div class="avatar" role="img" aria-label="Client portrait photo"></div>
      <span class="name">Jenna Cole</span><span class="role">Lorem ipsum</span><span class="stars">★★★★★</span>
    </div>
  </div>

  <p class="abs quote" style="left:777px;top:3016px">Lorem ipsum dolor sit amet, consectetuer adipiscing elit, sed diam nonu mmy nibh euismod tincidunt ut laoreet dolore magna aliquam erat volut pat. Ut wisi enim ad minim veniam, quis nostrud exerci.</p>
  <div class="abs profile" style="left:777px;top:3165px">
    <div class="avatar" role="img" aria-label="Client portrait photo"></div>
    <span class="name">Rosa Vint</span><span class="role">Lorem ipsum</span><span class="stars">★★★★★</span>
  </div>
</section>

<!-- GALLERY -->
<section>
  <div class="abs script center" style="top:3342px">Showcase</div>
  <h2 class="abs heading center" style="top:3369px">Photo Gallery</h2>

  <div class="abs tile" style="left:142px;top:3437px;width:250px;height:169px;background:radial-gradient(circle at 50% 55%,#7a8a6a,#3e6a1e 60%,#26420f)" role="img" aria-label="Photograph of a spray bottle product among green leaves"></div>
  <div class="abs tile" style="left:142px;top:3622px;width:250px;height:169px;background:linear-gradient(135deg,#d8c6a6,#b5703f 55%,#8a4e2a)" role="img" aria-label="Photograph of a boxed wheat heat bag product"></div>
  <div class="abs tile" style="left:406px;top:3437px;width:387px;height:354px;background:radial-gradient(circle at 40% 60%,#4d5238 0%,#8f9088 40%,#d9a88a 80%)" role="img" aria-label="Photograph of a branded cap and grey t-shirt on a table"></div>
  <div class="abs tile" style="left:806px;top:3437px;width:252px;height:169px;background:radial-gradient(circle,#a98a8a,#a48b62 55%,#7d6440)" role="img" aria-label="Photograph of branded drink coolers on dried leaves"></div>
  <div class="abs tile" style="left:806px;top:3622px;width:252px;height:169px;background:linear-gradient(135deg,#8a7458,#d9d2c4 50%,#5a6d9a)" role="img" aria-label="Photograph of a gift box with wellness products"></div>
</section>

<!-- FOOTER -->
<footer>
  <svg class="abs footer-edge" viewBox="0 0 1200 60" preserveAspectRatio="none" aria-hidden="true">
    <path d="M0 30 L40 26 L70 34 L110 22 L150 32 L200 20 L240 30 L290 24 L330 35 L380 21 L430 30 L480 23 L530 33 L580 20 L630 31 L690 24 L740 34 L790 22 L840 30 L900 25 L950 34 L1000 21 L1050 31 L1100 24 L1150 33 L1200 26 L1200 60 L0 60 Z" fill="var(--night)"/>
  </svg>
  <div class="abs footer">
    <div class="abs footer-brand" style="top:208px;left:144px">THE WELLNESS BARN</div>
  </div>
  <div class="footer">
    <h4 style="left:406px">Quick Links</h4>
    <span class="footer-link" style="top:4106px">» Home</span>
    <span class="footer-link" style="top:4136px">» Services</span>
    <span class="footer-link" style="top:4167px">» About Us</span>
    <span class="footer-link" style="top:4197px">» Timetable</span>
    <span class="footer-link" style="top:4227px">» Contact Us</span>

    <h4 style="left:597px">Contact Details</h4>
    <div class="contact-row" style="top:4104px">
      <svg width="14" height="16" viewBox="0 0 14 16" fill="none" stroke="#fff" stroke-width="1.4"><path d="M7 15s5-5 5-9A5 5 0 0 0 2 6c0 4 5 9 5 9z"/><circle cx="7" cy="6" r="1.8"/></svg>
      <div>14/22 Ridge Creek Road,<br>Fernvale, QLD 4306</div>
    </div>
    <div class="contact-row" style="top:4155px">
      <svg width="14" height="14" viewBox="0 0 14 14" fill="none" stroke="#fff" stroke-width="1.4"><path d="M3 1l2.5 3-1.5 1.5c1 2 2.5 3.5 4.5 4.5L10 8.5 13 11l-1.5 2C6 13 1 8 1 2.5z"/></svg>
      <div>Phone<br>07 5550 1842</div>
    </div>
    <div class="contact-row" style="top:4206px">
      <svg width="15" height="12" viewBox="0 0 15 12" fill="none" stroke="#fff" stroke-width="1.4"><rect x="1" y="1" width="13" height="10" rx="1"/><path d="M1 2l6.5 5L14 2"/></svg>
      <div>Email<br>hello@wellnessbarn.com.au</div>
    </div>

    <h4 style="left:857px">Locations</h4>
  </div>
  <div class="abs map" role="img" aria-label="Map showing the clinic location"></div>

  <div class="abs bottom-bar"><p>© 2025 THE WELLNESS BARN. All Rights Reserved.</p></div>
  <div class="abs social" style="left:960px"></div>
  <div class="abs social" style="left:996px"></div>
  <div class="abs social" style="left:1030px"></div>
</footer>

</body>
</html>
```